I would like a minimalist clean and uncluttered website design.
Initially, I would like to see a front page only and would then like to build on the project front there.
DLW logo file with no background is attached, can be grey scale if the designer wishes.
I would like the front page to speak about the company's ethos and goals and I will need to put a great deal of thought into this to ensure it has the desired impact with the content on the subsequent pages.
The paragraph below gives a bit of an idea as to what this will include.
"DLW is a technology company providing approachable IT products and services to business:
With the overwhelming advancements in technology, businesses often find it difficult to determine what is available and what best suits their businesses specific needs.
We can assist business with their IT infrustucture, devices, software in procurement, installation, training, cost control as well as ongoing administration and support. We also keep our Clients informed of new technology and products which can benefit them"
Target Market(s)
Business, Health, Education, Professional Practices. Target age would be around 30 plus either male or female. Office administration level through Managing Directors. English speaking.
Look and feel
Each slider illustrates characteristics of the customer's brand and the style your logo design should communicate.

```html
<!DOCTYPE html>
<html lang="en">
<head>
<meta charset="utf-8">
<title>DLW – Approachable IT for Business</title>
<link href="https://fonts.googleapis.com/css2?family=Roboto+Condensed:wght@400;700&family=Arimo:wght@400;700&display=swap" rel="stylesheet">
<style>
:root{
  --navy:#3b4d80;
  --navy-dark:#32446f;
  --green:#8cb24a;
  --green-band:#8aad55;
  --lime:#a4d04a;
  --ink:#3b4d80;
  --text:#555a63;
  --light:#f7f7f7;
  --cream:#f4f6e4;
  --white:#ffffff;
}
*{box-sizing:border-box;margin:0;padding:0}
html,body{width:688px;height:1200px;overflow:hidden;background:var(--white)}
body{position:relative;font-family:"Arimo",Arial,sans-serif;color:var(--text)}
a{color:inherit;text-decoration:none}
.abs{position:absolute}

/* top bar */
.topbar{left:0;top:0;width:688px;height:30px;background:var(--navy)}
.util-links{left:65px;top:10px;font-size:7px;color:var(--white)}
.util-links span{margin:0 4px}
.main-nav{top:12px;left:0;width:688px;font-family:"Roboto Condensed",sans-serif;font-size:7px;color:var(--white);text-transform:uppercase}
.main-nav a{position:absolute;white-space:nowrap}
.main-nav a.active{color:var(--lime)}

/* hero */
.hero{left:0;top:30px;width:688px;height:300px;background:linear-gradient(100deg,#e9ecef 0%,#f4f5f6 30%,#c9d2dc 55%,#8d9aa8 75%,#d5d9de 100%)}
.brand{left:64px;top:41px;display:flex;align-items:center;gap:6px}
.brand-square{width:32px;height:32px;background:var(--green)}
.brand-name{font-family:"Arimo",sans-serif;font-size:17px;color:#5b5f66;letter-spacing:.3px}
.hero-caption{left:65px;top:209px;width:248px;height:72px;background:var(--green);color:var(--white);padding:10px 10px 0 10px;font-size:11.5px;line-height:17.5px}
.hero-caption .more{position:absolute;right:12px;bottom:12px;font-size:6.5px}
.slide-btn{top:292px;width:29px;height:27px;display:flex;align-items:center;justify-content:center}
.slide-prev{left:65px;background:var(--navy)}
.slide-next{left:99px;background:var(--green)}

/* about */
.about-title{left:0;top:380px;width:688px;text-align:center;font-family:"Roboto Condensed",sans-serif;font-size:14.5px;color:var(--ink)}
.about-title em{font-style:normal;color:var(--green)}
.about-text{left:60px;top:418px;width:568px;text-align:center;font-size:7.2px;line-height:13.3px;color:var(--text)}
.about-text em{font-style:normal;color:var(--green)}

/* services */
.services{left:0;top:494px;width:688px;height:185px;background:var(--light)}
.services-title{left:0;top:517px;width:688px;text-align:center;font-family:"Roboto Condensed",sans-serif;font-size:14px;color:var(--ink)}
.service{top:557px;width:120px;text-align:center;font-family:"Roboto Condensed",sans-serif;font-size:7.5px;line-height:10.5px;color:var(--ink)}
.service .circle{width:67px;height:67px;border-radius:50%;background:var(--navy);margin:0 auto 8px;display:flex;align-items:center;justify-content:center}
.service .circle.green{background:var(--green)}

/* news & testimonials */
.news-band{left:0;top:679px;width:688px;height:320px;background:linear-gradient(160deg,#92b35c 0%,#87a953 50%,#8eaf58 100%)}
.news-title{left:0;top:703px;width:688px;text-align:center;font-family:"Roboto Condensed",sans-serif;font-size:13.5px;color:var(--white)}
.news-item{left:64px;width:260px;height:46px}
.date-box{position:absolute;left:0;top:0;width:52px;height:45px;background:var(--cream);text-align:center;color:#5e7a26;font-family:"Roboto Condensed",sans-serif}
.date-box b{display:block;font-size:12px;margin-top:7px}
.date-box small{display:block;font-size:8px;margin-top:2px;color:#555}
.news-head{position:absolute;left:66px;top:-1px;font-size:9.5px;color:var(--white);white-space:nowrap}
.news-body{position:absolute;left:66px;top:21px;width:190px;font-size:6.5px;line-height:10.5px;color:var(--white)}
.divider{left:349px;top:742px;height:205px;border-left:1px dashed rgba(255,255,255,.7)}
.testimonial{left:383px;width:240px;height:46px}
.portrait{position:absolute;left:0;top:0;width:50px;height:43px;border:2px solid var(--white);background:linear-gradient(135deg,#c9c2b8,#8b8176)}
.quote{position:absolute;left:66px;top:-1px;width:177px;font-size:6.5px;line-height:10.8px;color:var(--white)}
.author{position:absolute;right:-3px;top:48px;font-size:6.5px;color:#2f3a1a;white-space:nowrap}
.view-all{top:955px;font-size:7px;color:var(--white)}

/* footer */
.footer{left:0;top:999px;width:688px;height:176px;background:var(--navy)}
.foot-col{top:1017px}
.foot-col h3{font-family:"Roboto Condensed",sans-serif;font-weight:400;font-size:10px;color:var(--lime);margin-bottom:9px}
.foot-col ul{list-style:none;font-size:7px;line-height:12.7px;color:var(--white)}
.contact-list li span{display:inline-block;width:26px}
.mail-head{font-family:"Roboto Condensed",sans-serif;font-size:10px;color:var(--lime);margin:8px 0 3px}
.bottombar{left:0;top:1175px;width:688px;height:25px;background:var(--navy-dark)}
.copyright{left:64px;top:1183px;font-size:7px;color:var(--white)}
.follow{left:515px;top:1183px;font-size:7px;color:var(--white)}
.social{top:1177px;width:20px;height:20px;border-radius:3px}
</style>
</head>
<body>

<div class="abs topbar"></div>
<div class="abs util-links"><a href="#">Help Desk</a><span>|</span><a href="#">Sign in</a><span>|</span><a href="#">Register</a></div>
<nav class="abs main-nav">
  <a class="active" href="#" style="left:338px">Home</a>
  <a href="#" style="left:376px">About Us</a>
  <a href="#" style="left:426px">Services</a>
  <a href="#" style="left:474px">Our Clients</a>
  <a href="#" style="left:532px">News &amp; Blog</a>
  <a href="#" style="left:591px">Contact Us</a>
</nav>

<section class="abs hero" role="img" aria-label="Photo of a bright office with a smiling support agent wearing a headset at a monitor and colleagues working behind"></section>
<div class="abs brand"><div class="brand-square"></div><span class="brand-name">datalinkworks</span></div>
<div class="abs hero-caption">DLW is a technology company providing approachable IT products and services to business<a class="more" href="#">Learn more &gt;&gt;</a></div>
<a class="abs slide-btn slide-prev" href="#" aria-label="Previous slide"><svg width="10" height="14" viewBox="0 0 10 14"><path d="M7 1 2 7l5 6" fill="none" stroke="#fff" stroke-width="1.3"/></svg></a>
<a class="abs slide-btn slide-next" href="#" aria-label="Next slide"><svg width="10" height="14" viewBox="0 0 10 14"><path d="M3 1l5 6-5 6" fill="none" stroke="#fff" stroke-width="1.3"/></svg></a>

<h2 class="abs about-title">Something about <em>DLW</em></h2>
<p class="abs about-text"><em>DLW is a technology</em> company providing approachable IT products and services to business:<br>With the overwhelming advancements in technology, businesses often find it difficult to determine what is available and what best suits their businesses specific needs.<br>We can assist business with their IT infrustucture, devices, software in procurement, installation, training, cost control as well as ongoing administration and support. We<br>also keep our Clients informed of new technology and products which can benefit them"</p>

<section class="abs services"></section>
<h2 class="abs services-title">Services We Are Providing</h2>
<div class="abs service" style="left:59px">
  <div class="circle green"><svg width="30" height="24" viewBox="0 0 30 24"><rect x="1" y="5" width="28" height="18" rx="2" fill="#fff"/><rect x="10" y="1" width="10" height="5" rx="1" fill="none" stroke="#fff" stroke-width="2"/><rect x="13" y="11" width="4" height="3" fill="#8cb24a"/></svg></div>
  IT infrustucture</div>
<div class="abs service" style="left:174px">
  <div class="circle"><svg width="20" height="30" viewBox="0 0 20 30"><rect x="1" y="1" width="18" height="28" rx="3" fill="#fff"/><rect x="4" y="4" width="12" height="10" fill="#3b4d80"/><circle cx="10" cy="21" r="4" fill="none" stroke="#3b4d80" stroke-width="2"/></svg></div>
  IT devices</div>
<div class="abs service" style="left:289px">
  <div class="circle"><svg width="30" height="28" viewBox="0 0 30 28"><path d="M15 9 4 5 1 10l11 4zM15 9l11-4 3 5-11 4zM5 12v10l10 5 10-5V12l-10 4z" fill="#fff"/></svg></div>
  software in procurement<br>&amp;  installation</div>
<div class="abs service" style="left:404px">
  <div class="circle"><svg width="32" height="30" viewBox="0 0 32 30"><g fill="#fff"><rect x="14" y="4" width="16" height="4" rx="1"/><rect x="14" y="10" width="16" height="4" rx="1"/><rect x="14" y="16" width="16" height="4" rx="1"/><rect x="14" y="22" width="16" height="4" rx="1"/><circle cx="10" cy="19" r="9"/></g><text x="10" y="23" font-size="11" font-family="Arimo,sans-serif" text-anchor="middle" fill="#3b4d80">$</text></svg></div>
  cost control</div>
<div class="abs service" style="left:517px">
  <div class="circle"><svg width="30" height="30" viewBox="0 0 30 30"><path d="M14 5H3v22h22V16" fill="none" stroke="#fff" stroke-width="2.5"/><path d="M24 2l4 4-13 13-5 1 1-5z" fill="#fff"/></svg></div>
  ongoing administration<br>and support</div>

<section class="abs news-band" role="img" aria-label="Faded photo of a business meeting with a rising chart arrow under a green tint"></section>
<h2 class="abs news-title">Latest News and Testimonials</h2>

<article class="abs news-item" style="top:747px"><div class="date-box"><b>OCT 22</b><small>2013</small></div><h3 class="news-head">News Headline Goes Here</h3><p class="news-body">DLW is a technology company providing approachable IT products and services to business:</p></article>
<article class="abs news-item" style="top:821px"><div class="date-box"><b>OCT 22</b><small>2013</small></div><h3 class="news-head">News Headline Goes Here</h3><p class="news-body">DLW is a technology company providing approachable IT products and services to business:</p></article>
<article class="abs news-item" style="top:896px"><div class="date-box"><b>OCT 22</b><small>2013</small></div><h3 class="news-head">News Headline Goes Here</h3><p class="news-body">DLW is a technology company providing approachable IT products and services to business:</p></article>
<a class="abs view-all" href="#" style="left:130px">View All &nbsp;&gt;&gt;</a>

<div class="abs divider"></div>

<blockquote class="abs testimonial" style="top:748px"><div class="portrait" role="img" aria-label="Portrait of a client wearing glasses"></div><p class="quote">Lorem Ipsum is simply dummy text of the printing and typesetting industry. Lorem Ipsum has been the industry's standard dummy text ever since the 1500s, when</p><cite class="author" style="font-style:normal">Miss Clara ( CEO of Company Name )</cite></blockquote>
<blockquote class="abs testimonial" style="top:822px"><div class="portrait" role="img" aria-label="Portrait of a grey-haired client"></div><p class="quote">Lorem Ipsum is simply dummy text of the printing and typesetting industry. Lorem Ipsum has been the industry's standard dummy text ever since the 1500s, when</p><cite class="author" style="font-style:normal">Mr. Holt ( CEO of Company Name )</cite></blockquote>
<blockquote class="abs testimonial" style="top:897px"><div class="portrait" role="img" aria-label="Portrait of a client in a suit"></div><p class="quote">Lorem Ipsum is simply dummy text of the printing and typesetting industry. Lorem Ipsum has been the industry's standard dummy text ever since the 1500s, when</p><cite class="author" style="font-style:normal">Mr. Rowan ( CEO of Company Name )</cite></blockquote>
<a class="abs view-all" href="#" style="left:449px">View All &nbsp;&gt;&gt;</a>

<footer class="abs footer"></footer>
<div class="abs foot-col" style="left:64px"><h3>Quick Links</h3><ul><li>Home</li><li>About us</li><li>Services</li><li>Technology</li><li>News and Blog</li><li>Contact us</li><li>Privacy lokicy</li><li>Terms of Use</li></ul></div>
<div class="abs foot-col" style="left:210px"><h3>Services</h3><ul><li>IT Infarastructure</li><li>Devices Managment</li><li>Cost Managment</li><li>software in procurement</li><li>Software Installation</li><li>ongoing Adminstration</li><li>&amp; Support</li></ul></div>
<div class="abs foot-col" style="left:359px"><h3>Online Support</h3><ul><li>Our Customer Care</li><li>Information</li><li>Cost Managment</li><li>Request a Quote</li><li>Inquery</li><li>ongoing Support</li><li>Newsletter</li></ul></div>
<div class="abs foot-col" style="left:506px"><h3>Contact us</h3><ul class="contact-list"><li><span>PH. NO</span>: 000-0000-000</li><li><span>Email</span>: info@dlwmail.com</li><li><span>Fax</span>: info@dlwmail.com</li></ul><div class="mail-head">Mailing Address :</div><ul><li>Company Mailling Address</li><li>Goes Here :</li></ul></div>

<div class="abs bottombar"></div>
<div class="abs copyright">Copyright © 2013 DLW.com</div>
<div class="abs follow">FOLLOW US :</div>
<a class="abs social" href="#" aria-label="Social profile one" style="left:563px;background:#3f63a8"></a>
<a class="abs social" href="#" aria-label="Social profile two" style="left:587px;background:#3c9fd8"></a>
<a class="abs social" href="#" aria-label="Social profile three" style="left:611px;background:#4a86d0"></a>

</body>
</html>
```